App Design Project

We are building an app and looking for design help on an existing template. We will also need a style guide. For more information, there is a website which outlines the assignment with visuals. Go here:

http://www.brivalora.com/

Industry/Entity Type

Building

```html
<!DOCTYPE html>
<html lang="en">
<head>
<meta charset="utf-8">
<title>Activities</title>
<link href="https://fonts.googleapis.com/css2?family=Lobster&family=Lato:wght@300;400;700&display=swap" rel="stylesheet">
<style>
  :root {
    --page-bg: #16181b;
    --screen-bg: #141414;
    --screen-bg-light: #262626;
    --accent: #f7a21a;
    --accent-dark: #e07f00;
    --accent-text: #2a1a00;
    --button-dark: #3a3a3a;
    --button-darker: #1c1c1c;
    --button-text: #8a8a8a;
    --status-text: #f2f2f2;
    --parchment-light: #e8d3a4;
    --parchment-mid: #c9a86a;
    --parchment-edge: #5a3a18;
    --ink: #2c1c0e;
    --ink-soft: #4a3520;
    --female: #d43a8a;
    --male: #2a7fc0;
    --divider: #3a3a3a;
  }
  * { box-sizing: border-box; margin: 0; padding: 0; }
  html, body { width: 923px; height: 1200px; overflow: hidden; background: var(--page-bg); }
  body { position: relative; font-family: "Lato", sans-serif; }

  .screen {
    position: absolute; left: 141px; top: 32px; width: 640px; height: 1136px;
    background:
      repeating-linear-gradient(115deg, rgba(255,255,255,0.025) 0 2px, transparent 2px 7px),
      radial-gradient(ellipse at 50% 35%, var(--screen-bg-light), var(--screen-bg) 75%);
    overflow: hidden;
  }

  .status-bar {
    position: absolute; left: 0; top: 0; width: 100%; height: 40px;
    background: #000; color: var(--status-text);
    font: 700 22px "Lato", sans-serif;
    display: flex; align-items: center; justify-content: space-between; padding: 0 14px;
  }
  .status-bar .carrier { display: flex; align-items: center; gap: 6px; width: 160px; }
  .signal { display: flex; align-items: flex-end; gap: 2px; height: 14px; }
  .signal i { display: block; width: 3px; background: var(--status-text); }
  .status-icons { width: 160px; display: flex; justify-content: flex-end; align-items: center; gap: 8px; }

  .nav-bar { position: absolute; left: 0; top: 40px; width: 100%; height: 126px; border-bottom: 2px solid var(--divider); }
  .nav-title {
    position: absolute; left: 0; right: 0; top: 40px; text-align: center;
    font: 48px "Lobster", cursive; color: var(--accent);
  }
  .round-btn {
    position: absolute; width: 66px; height: 66px; border-radius: 50%;
    background: radial-gradient(circle at 50% 30%, var(--button-dark), var(--button-darker));
    box-shadow: 0 2px 4px rgba(0,0,0,0.8), inset 0 1px 0 rgba(255,255,255,0.12);
    display: flex; align-items: center; justify-content: center;
  }
  .nav-back { left: 50px; top: 37px; }
  .nav-sort { left: 519px; top: 37px; }

  .segments { position: absolute; left: 37px; top: 193px; width: 566px; height: 65px; display: flex; gap: 13px; }
  .segment {
    flex: 1; border-radius: 33px; display: flex; align-items: center; justify-content: center;
    font: italic 26px "Lobster", cursive;
    background: linear-gradient(#454545, #202020); color: #1a1a1a;
    text-shadow: 0 1px 0 rgba(255,255,255,0.12);
    box-shadow: 0 2px 4px rgba(0,0,0,0.8), inset 0 1px 0 rgba(255,255,255,0.1);
  }
  .segment.is-active { background: linear-gradient(#ffb52e, var(--accent-dark)); color: var(--accent-text); text-shadow: none; }
  .segment.is-muted { color: #2a2a2a; }

  .activity-card {
    position: absolute; left: 28px; width: 579px; height: 269px; border-radius: 6px;
    background: radial-gradient(ellipse 60% 65% at 50% 48%, var(--parchment-light), var(--parchment-mid) 55%, var(--parchment-edge) 100%);
    box-shadow: 0 4px 10px rgba(0,0,0,0.8);
    color: var(--ink);
  }
  .card-title { position: absolute; left: 58px; top: 26px; font: 300 44px "Lato", sans-serif; color: var(--ink-soft); }
  .card-divider { position: absolute; left: 48px; right: 48px; top: 90px; height: 2px; background: rgba(60,40,20,0.35); }
  .venue { position: absolute; left: 58px; top: 115px; font: 400 27px "Lato", sans-serif; }
  .date, .time { position: absolute; left: 58px; font: 700 18px "Lato", sans-serif; }
  .date { top: 156px; }
  .time { top: 178px; }
  .expires { position: absolute; left: 58px; top: 217px; font: 400 13px "Lato", sans-serif; color: var(--ink-soft); }
  .gender-badge {
    position: absolute; left: 353px; top: 124px; width: 74px; height: 74px; border-radius: 50%;
    border: 3px solid #6a5430; background: radial-gradient(circle, #e2cd8e, #b59a58);
    display: flex; align-items: center; justify-content: center; font: 700 36px "Lato", sans-serif;
  }
  .gender-badge.female { color: var(--female); }
  .gender-badge.male { color: var(--male); }
  .username { position: absolute; left: 340px; width: 100px; text-align: center; top: 210px; font: 400 22px "Lato", sans-serif; }
  .chevron { position: absolute; left: 500px; top: 174px; }

  .tab-bar { position: absolute; left: 0; top: 1009px; width: 100%; height: 92px; }
  .tab {
    position: absolute; top: 0; width: 92px; height: 92px; border-radius: 50%;
    background: radial-gradient(circle at 50% 30%, #3c3c3c, #161616);
    box-shadow: 0 3px 6px rgba(0,0,0,0.9), inset 0 1px 0 rgba(255,255,255,0.1);
    display: flex; align-items: center; justify-content: center; text-align: center;
    font: 400 19px/1.05 "Lato", sans-serif; color: var(--button-text);
  }
  .tab.is-active { background: radial-gradient(circle at 50% 30%, #ffb52e, var(--accent-dark)); color: var(--accent-text); font-weight: 700; }
  .tab.is-active::before {
    content: ""; position: absolute; top: -12px; left: 36px; width: 20px; height: 20px;
    border-radius: 50% 50% 0 50%; transform: rotate(45deg); background: #ffb52e;
  }
</style>
</head>
<body>
<main class="screen">
  <header class="status-bar">
    <div class="carrier">
      <span class="signal"><i style="height:5px"></i><i style="height:7px"></i><i style="height:9px"></i><i style="height:11px"></i><i style="height:13px"></i></span>
      Valt
    </div>
    <div class="clock">4:20 PM</div>
    <div class="status-icons">
      <svg width="44" height="20" viewBox="0 0 44 20"><path d="M6 10 L14 2 L11 18 Z" fill="#f2f2f2"/><circle cx="30" cy="10" r="7" fill="none" stroke="#f2f2f2" stroke-width="2"/></svg>
      <svg width="44" height="20" viewBox="0 0 44 20"><rect x="1" y="3" width="38" height="14" rx="3" fill="none" stroke="#f2f2f2" stroke-width="2"/><rect x="4" y="6" width="32" height="8" fill="#f2f2f2"/><rect x="40" y="7" width="3" height="6" fill="#f2f2f2"/></svg>
    </div>
  </header>

  <nav class="nav-bar">
    <div class="round-btn nav-back" aria-label="Back">
      <svg width="30" height="30" viewBox="0 0 30 30"><path d="M16 5 L6 15 L16 25 M6 15 H25" fill="none" stroke="#0f0f0f" stroke-width="5" stroke-linecap="round" stroke-linejoin="round"/></svg>
    </div>
    <h1 class="nav-title">Activities</h1>
    <div class="round-btn nav-sort" aria-label="Sort">
      <svg width="30" height="34" viewBox="0 0 30 34"><path d="M15 3 L5 13 H25 Z M15 31 L5 21 H25 Z" fill="#111"/></svg>
    </div>
  </nav>

  <div class="segments">
    <div class="segment is-active">Search All</div>
    <div class="segment">People</div>
    <div class="segment is-muted">Groups</div>
  </div>

  <article class="activity-card" style="top:298px">
    <h2 class="card-title">Velvet Horror Show</h2>
    <div class="card-divider"></div>
    <p class="venue">Old Town Cinema</p>
    <p class="date">October 8, 2012</p>
    <p class="time">12:00 AM</p>
    <p class="expires">Expires in 6 hrs, 39 mins</p>
    <div class="gender-badge female">♀</div>
    <p class="username">Nancy14</p>
    <svg class="chevron" width="36" height="54" viewBox="0 0 36 54"><path d="M8 6 L28 27 L8 48" fill="none" stroke="#3a2610" stroke-width="7" stroke-linecap="round" stroke-linejoin="round"/></svg>
  </article>

  <article class="activity-card" style="top:600px">
    <h2 class="card-title">Velvet Horror Show</h2>
    <div class="card-divider"></div>
    <p class="venue">Old Town Cinema</p>
    <p class="date">October 8, 2012</p>
    <p class="time">12:00 AM</p>
    <p class="expires">Expires in 6 hrs, 39 mins</p>
    <div class="gender-badge male">♂</div>
    <p class="username">Joe29</p>
    <svg class="chevron" width="36" height="54" viewBox="0 0 36 54"><path d="M8 6 L28 27 L8 48" fill="none" stroke="#3a2610" stroke-width="7" stroke-linecap="round" stroke-linejoin="round"/></svg>
  </article>

  <footer class="tab-bar">
    <div class="tab is-active" style="left:37px">Search</div>
    <div class="tab" style="left:155px">New<br>Post</div>
    <div class="tab" style="left:271px">MSGS</div>
    <div class="tab" style="left:390px">Alerts</div>
    <div class="tab" style="left:508px">More</div>
  </footer>
</main>
</body>
</html>
```